Helicopter Company - Rotavia Sweden

I need a new design and implementation of a webpage. We rent helicopters and are also starting a school. We havre started a wordpress but the page is very ugly. Need a complete update. Logo exist already. We also have some pictures of helicotopers. We are open for all designs but it is important that it looks professionel, is eassy to update and will give an impression och structure and dicipline.
Updates

Target Market(s)

Customers that what to get a certificate to fly. It is expensive so it’s either people with a lot of money or people with a big dream. It is very serious business.

Industry/Entity Type

www.rotavia-demo.se

Coding

Coded - Design and coding required

Number of Pages Required

4 page

Font styles to use
Sans Serif

Colors
0054AA
0677BA
7BADD7
CADEEF
E8F1F8

Requirements
Must have
• A easy page the gives a feeling of seriousness and

```html
<!DOCTYPE html>
<html lang="sv">
<head>
<meta charset="utf-8">
<title>Rotavia Sweden – Helikopteruthyrning &amp; flygskola</title>
<link href="https://fonts.googleapis.com/css2?family=Prata&family=Plus+Jakarta+Sans:wght@400;500;600;700&display=swap" rel="stylesheet">
<style>
:root{
  --navy:#172e4c;
  --navy-dark:#132740;
  --blue:#0677ba;
  --blue-bright:#1e8fd6;
  --cta:#36a4db;
  --sky-light:#cadeef;
  --ice:#eef2f8;
  --text:#2b2f36;
  --muted:#5d636d;
  --white:#ffffff;
  --serif:"Prata", Georgia, serif;
  --sans:"Plus Jakarta Sans", Arial, sans-serif;
}
*{box-sizing:border-box;margin:0;padding:0}
html,body{width:1200px;height:2810px;overflow:hidden}
body{position:relative;font-family:var(--sans);color:var(--text);background:var(--white)}
.abs{position:absolute}

/* top bar */
.topbar{left:0;top:0;width:1200px;height:40px;background:var(--navy);color:#e6ecf3;font-size:10.5px;font-weight:500}
.topbar span{position:absolute;top:14px}
.topbar .dot{position:absolute;top:13px;width:12px;height:12px;border:1.5px solid #e6ecf3;border-radius:50%}

/* hero */
.hero{left:0;top:40px;width:1200px;height:666px;
  background:
   radial-gradient(ellipse 420px 360px at 330px 260px,rgba(255,255,255,.97),rgba(255,255,255,.6) 55%,rgba(255,255,255,0) 80%),
   radial-gradient(ellipse 300px 420px at 150px 520px,rgba(255,255,255,.95),rgba(255,255,255,0) 75%),
   radial-gradient(ellipse 180px 140px at 840px 420px,#1b4f9a,rgba(27,79,154,0) 80%),
   linear-gradient(110deg,#d9e7f3 0%,#7fb6e3 40%,#2f8ed6 65%,#0f7ccf 100%)}
.logo{font-family:var(--serif);color:var(--text);letter-spacing:1px;display:flex;align-items:center;gap:8px}
.logo i{display:block;width:10px;height:10px;border-radius:50%;background:var(--navy)}
.nav a{position:absolute;top:83px;font-size:13px;font-weight:500;color:var(--white);text-decoration:none}
.nav .sep{position:absolute;top:80px;width:1px;height:20px;background:rgba(255,255,255,.35)}
.hero-title{left:105px;top:284px;font-family:var(--serif);font-size:42px;color:#111;font-weight:400}
.hero-title em{font-style:normal;color:var(--blue)}
.hero-sub{left:105px;top:340px;font-family:var(--serif);font-size:24px;color:#444}
.btn-dark{display:flex;align-items:center;justify-content:center;background:var(--navy);color:var(--white);border-radius:24px;font-size:13px;font-weight:700;letter-spacing:.2px}
.scroll{left:582px;top:584px;width:36px;text-align:center;font-family:var(--sans);font-size:12px;font-weight:700;color:#1c2838;line-height:20px}

/* about */
.eyebrow{font-size:11px;font-weight:600;letter-spacing:1.2px;color:#333}
.h2{font-family:var(--serif);font-size:40px;line-height:45px;color:#111;font-weight:400;letter-spacing:.5px}
.body-text{font-size:13px;line-height:16px;color:#3b3f46}
.photo{border-radius:12px}

/* services */
.services{left:0;top:1110px;width:1200px;height:505px;background:var(--navy)}
.card-title{font-family:var(--serif);font-size:21px;color:var(--white)}
.card-text{font-size:12.5px;line-height:18px;color:#e3e9f1}
.more{font-size:12px;color:#9fb0c4;display:flex;align-items:center;gap:8px}

/* why */
.checks li{list-style:none;display:flex;align-items:center;gap:10px;font-size:13px;color:#444;height:22.5px}

/* cta */
.cta{left:0;top:2179px;width:1200px;height:276px}
.cta-title{left:349px;top:2263px;font-family:var(--serif);font-size:40px;color:var(--white)}
.cta-sub{left:349px;top:2320px;font-size:22px;color:var(--white)}
.btn-light{left:917px;top:2281px;width:178px;height:56px;background:var(--white);border-radius:4px;color:var(--cta);font-size:16px;display:flex;align-items:center;justify-content:center}

/* footer */
.footer-bg{left:0;top:2422px;width:1200px;height:388px;background:var(--ice)}
.f-head{font-size:11.5px;font-weight:700;color:#111}
.f-list{font-size:10px;color:#222;line-height:21px}
.f-list li{list-style:none;display:flex;align-items:center;gap:4px}
.f-list li::before{content:"";width:6px;height:6px;border-radius:50%;background:#8f959e}
.f-text{font-size:10px;color:#222;line-height:14px}
.social-dot{width:9px;height:9px;border-radius:50%;background:#3b4a66}
</style>
</head>
<body>

<!-- top bar -->
<div class="abs topbar">
  <span style="left:105px">FRÅGOR? MAILA ELLER RING!</span>
  <span style="left:283px">+46 700 123 456</span>
  <span style="left:409px">INFO@ROTAVIA-DEMO.SE</span>
  <div class="dot" style="left:1060px"></div>
  <div class="dot" style="left:1083px"></div>
</div>

<!-- hero -->
<div class="abs hero" role="img" aria-label="Blå helikopter i flykt mot en himmel med vita moln"></div>
<div class="abs logo" style="left:105px;top:66px;font-size:30px"><i></i>ROTAVIA</div>
<nav class="nav">
  <a class="abs" style="left:840px;color:#8fc3ea">START</a>
  <div class="sep" style="left:894px"></div>
  <a class="abs" style="left:910px">OM OSS</a>
  <div class="sep" style="left:975px"></div>
  <a class="abs" style="left:990px">KONTAKT</a>
  <div class="sep" style="left:1066px"></div>
  <svg class="abs" style="left:1081px;top:84px" width="13" height="13" viewBox="0 0 13 13" fill="none" stroke="#fff" stroke-width="1.6"><circle cx="7.5" cy="5.5" r="4.2"/><path d="M4.5 8.5 1 12"/></svg>
</nav>
<h1 class="abs hero-title">Välkommen till <em>Rotavia</em></h1>
<p class="abs hero-sub">Hyr din helikopter av oss!</p>
<div class="abs btn-dark" style="left:105px;top:403px;width:174px;height:44px">LÄS MER OM OSS!</div>
<div class="abs scroll">
  <svg width="22" height="52" viewBox="0 0 22 52" fill="none" stroke="#1c2838" stroke-width="1.6"><circle cx="11" cy="2" r="1" fill="#1c2838"/><circle cx="11" cy="8" r="1" fill="#1c2838"/><rect x="3" y="14" width="16" height="26" rx="8"/><path d="M11 20v6"/></svg>
  <div>SCROLL<br>DOWN</div>
</div>

<!-- about -->
<p class="abs eyebrow" style="left:105px;top:777px">WELCOME TO ROTAVIA FLIGHT</p>
<h2 class="abs h2" style="left:105px;top:803px;width:420px">We are the best aviation and flight school in town</h2>
<p class="abs body-text" style="left:105px;top:953px;width:480px">Donec vitae fermentum ante. Nullam neque purus, luctus vel ipsum ut, aliquam fringilla ex. Vivamus tincidunt dolor id tristique scelerisque.</p>
<div class="abs btn-dark" style="left:105px;top:1012px;width:144px;height:44px">ABOUT US</div>
<div class="abs" style="left:676px;top:769px;width:418px;height:246px;border:2px solid var(--blue);border-radius:14px"></div>
<div class="abs photo" style="left:641px;top:783px;width:439px;height:273px;background:linear-gradient(180deg,#cfe0f3 0%,#9fc0e3 35%,#6a7480 60%,#8b8f93 100%)" role="img" aria-label="Svart helikopter bredvid en limegrön sportbil på en bana"></div>

<!-- services -->
<section class="abs services"></section>
<div class="abs photo" style="left:106px;top:1164px;width:310px;height:225px;background:linear-gradient(135deg,#b49b7c,#7f6a55)" role="img" aria-label="Hammare och spikar på träyta"></div>
<div class="abs photo" style="left:445px;top:1164px;width:309px;height:225px;background:linear-gradient(180deg,#3f7fcf 0%,#2d5a3c 45%,#6e8a3a 100%)" role="img" aria-label="Mörkblå helikopter på en gräsmatta vid skogskant"></div>
<div class="abs photo" style="left:785px;top:1164px;width:309px;height:225px;background:linear-gradient(90deg,#5a6068,#d9dde2 50%,#eceef0)" role="img" aria-label="Helikopter i en ljus hangar"></div>

<h3 class="abs card-title" style="left:121px;top:1410px">Rental</h3>
<p class="abs card-text" style="left:121px;top:1445px;width:272px">We rent out helicopters. Among other things, we have a brand new Skyline S44 Falcon 1 with 130 hours on the tacho.&nbsp; The requirement for you is that you pay an advance and can present a medical and a valid certificate.</p>
<div class="abs more" style="left:121px;top:1552px">Learn More <svg width="14" height="8" viewBox="0 0 14 8" fill="none" stroke="#9fb0c4" stroke-width="1.5"><path d="M0 4h12M9 1l3 3-3 3"/></svg></div>

<h3 class="abs card-title" style="left:460px;top:1410px">Our Helicopters!</h3>
<p class="abs card-text" style="left:460px;top:1445px;width:272px">We rent helicopters of the brand Skyline S44. Falcon 1 and Kestrel 2. They are identical on the outside but differ slightly technically. One is from 2021 and the other has a few more years left.</p>
<div class="abs more" style="left:460px;top:1552px">Learn More <svg width="14" height="8" viewBox="0 0 14 8" fill="none" stroke="#9fb0c4" stroke-width="1.5"><path d="M0 4h12M9 1l3 3-3 3"/></svg></div>

<h3 class="abs card-title" style="left:800px;top:1410px">Other types of helicopter jobs</h3>
<p class="abs card-text" style="left:800px;top:1445px;width:280px">We can take care of photo flights, inventory of, for example, bark beetles or game. We cooperate with various operators and depart by helicopter from southern Sweden!</p>
<div class="abs more" style="left:800px;top:1537px">Learn More <svg width="14" height="8" viewBox="0 0 14 8" fill="none" stroke="#9fb0c4" stroke-width="1.5"><path d="M0 4h12M9 1l3 3-3 3"/></svg></div>

<!-- why choose us -->
<div class="abs" style="left:172px;top:1800px;width:281px;height:229px;border:1.5px solid var(--blue);border-radius:12px"></div>
<div class="abs photo" style="left:105px;top:1685px;width:289px;height:294px;background:linear-gradient(160deg,#8a8f96,#2a2d33 55%,#1a1c20)" role="img" aria-label="Helikopterkabin i närbild i en hangar"></div>
<div class="abs photo" style="left:231px;top:1858px;width:288px;height:269px;background:linear-gradient(140deg,#f0d2ac,#e8c59b)" role="img" aria-label="Hand som håller ett vitt certifikatblad mot beige bakgrund"></div>

<p class="abs eyebrow" style="left:606px;top:1757px">WHY CHOOSE US</p>
<h2 class="abs h2" style="left:608px;top:1785px;width:420px">Student about the training team</h2>
<p class="abs body-text" style="left:608px;top:1896px;width:420px">This also meant we needed to provide a learning environment run by experienced and successful coaches.</p>
<ul class="abs checks" style="left:608px;top:1950px">
  <li><svg width="13" height="13" viewBox="0 0 13 13"><circle cx="6.5" cy="6.5" r="6.5" fill="#4a4f57"/><path d="M3.5 6.6l2 2 4-4" fill="none" stroke="#fff" stroke-width="1.5"/></svg>Professional teacher</li>
  <li><svg width="13" height="13" viewBox="0 0 13 13"><circle cx="6.5" cy="6.5" r="6.5" fill="#4a4f57"/><path d="M3.5 6.6l2 2 4-4" fill="none" stroke="#fff" stroke-width="1.5"/></svg>Have heen certified</li>
  <li><svg width="13" height="13" viewBox="0 0 13 13"><circle cx="6.5" cy="6.5" r="6.5" fill="#4a4f57"/><path d="M3.5 6.6l2 2 4-4" fill="none" stroke="#fff" stroke-width="1.5"/></svg>Quality of our research</li>
  <li><svg width="13" height="13" viewBox="0 0 13 13"><circle cx="6.5" cy="6.5" r="6.5" fill="#4a4f57"/><path d="M3.5 6.6l2 2 4-4" fill="none" stroke="#fff" stroke-width="1.5"/></svg>Breadth of our capabilities</li>
</ul>
<ul class="abs checks" style="left:871px;top:1950px">
  <li><svg width="13" height="13" viewBox="0 0 13 13"><circle cx="6.5" cy="6.5" r="6.5" fill="#4a4f57"/><path d="M3.5 6.6l2 2 4-4" fill="none" stroke="#fff" stroke-width="1.5"/></svg>Trustworthy</li>
  <li><svg width="13" height="13" viewBox="0 0 13 13"><circle cx="6.5" cy="6.5" r="6.5" fill="#4a4f57"/><path d="M3.5 6.6l2 2 4-4" fill="none" stroke="#fff" stroke-width="1.5"/></svg>High integrity</li>
  <li><svg width="13" height="13" viewBox="0 0 13 13"><circle cx="6.5" cy="6.5" r="6.5" fill="#4a4f57"/><path d="M3.5 6.6l2 2 4-4" fill="none" stroke="#fff" stroke-width="1.5"/></svg>Providing The best courses</li>
  <li><svg width="13" height="13" viewBox="0 0 13 13"><circle cx="6.5" cy="6.5" r="6.5" fill="#4a4f57"/><path d="M3.5 6.6l2 2 4-4" fill="none" stroke="#fff" stroke-width="1.5"/></svg>Providing The best courses</li>
</ul>

<!-- footer background + cta band -->
<div class="abs footer-bg"></div>
<svg class="abs cta" width="1200" height="276" viewBox="0 0 1200 276"><path d="M0 0H1200V243L600 276 0 243Z" fill="var(--cta)"/></svg>
<div class="abs" style="left:112px;top:2260px;width:96px;height:96px;border-radius:48px;background:rgba(255,255,255,.22)" role="img" aria-label="Ikon av pilothjälm med skyddsglasögon och mikrofon"></div>
<h2 class="abs cta-title">Like To Become A Pilot</h2>
<p class="abs cta-sub">Lorem ipsum dolor sit amet consectetuer</p>
<div class="abs btn-light">Become An Pilot</div>

<!-- footer -->
<div class="abs logo" style="left:105px;top:2490px;font-size:22px"><i style="width:8px;height:8px"></i>ROTAVIA</div>
<p class="abs" style="left:830px;top:2503px;font-size:9px;color:#222">Follow us on social media</p>
<div class="abs social-dot" style="left:964px;top:2505px"></div>
<div class="abs social-dot" style="left:1000px;top:2505px"></div>
<div class="abs social-dot" style="left:1037px;top:2505px"></div>
<div class="abs social-dot" style="left:1073px;top:2505px"></div>
<div class="abs" style="left:105px;top:2556px;width:997px;height:1px;background:#d6dbe3"></div>

<p class="abs f-head" style="left:105px;top:2610px">Links</p>
<ul class="abs f-list" style="left:105px;top:2636px">
  <li>www.padline-demo.se</li><li>www.skylineheli-demo.com</li><li>www.lindbyflyclub-demo.se/</li>
</ul>
<p class="abs f-head" style="left:278px;top:2610px">Partners</p>
<ul class="abs f-list" style="left:278px;top:2636px">
  <li>Padline</li><li>NHC</li><li>Mira's</li>
</ul>
<p class="abs f-head" style="left:409px;top:2610px">Opening hours</p>
<p class="abs f-text" style="left:409px;top:2640px">Monday - Sunday: 09 00 – 17 0<br>Other time according to agreement.</p>
<p class="abs f-head" style="left:629px;top:2610px">Contact information</p>
<p class="abs f-text" style="left:629px;top:2640px">Rotavia,<br>Lindby Airport,</p>
<p class="abs f-text" style="left:629px;top:2680px;display:flex;align-items:center;gap:5px"><svg width="11" height="11" viewBox="0 0 11 11"><circle cx="5.5" cy="5.5" r="5.5" fill="#8f959e"/><path d="M3.4 3c.3 1.9 2.1 4 4.2 4.5l.5-1-1.2-.6-.5.5c-.9-.4-1.5-1.1-1.8-1.9l.5-.5-.6-1.2z" fill="#fff"/></svg>+46 (0) 707 123 456</p>
<p class="abs f-text" style="left:629px;top:2701px;display:flex;align-items:center;gap:5px"><svg width="11" height="11" viewBox="0 0 11 11"><circle cx="5.5" cy="5.5" r="5.5" fill="#8f959e"/><rect x="2.8" y="3.6" width="5.4" height="3.8" fill="none" stroke="#fff" stroke-width=".9"/></svg>info@rotavia-demo.se</p>

<p class="abs f-head" style="left:829px;top:2608px">Enterprise</p>
<p class="abs" style="left:829px;top:2630px;font-size:9.5px;color:#222">Customized Programs For Businesses and Enterprise Teams</p>
<div class="abs" style="left:822px;top:2656px;width:279px;height:50px;background:var(--white);border-radius:25px"></div>
<p class="abs" style="left:845px;top:2675px;font-size:10px;color:#888">Enter your email ...</p>
<div class="abs" style="left:1006px;top:2665px;width:83px;height:34px;border-radius:17px;background:var(--blue-bright);color:#fff;font-size:10.5px;font-weight:600;display:flex;align-items:center;justify-content:center">Submit</div>
<div class="abs" style="left:831px;top:2719px;width:11px;height:11px;border:1px solid #777;border-radius:2px;background:#fff"></div>
<p class="abs" style="left:852px;top:2719px;font-size:8.5px;color:#222">Yes please, contact us for customized team programs</p>

<p class="abs" style="left:104px;top:2748px;font-size:8.5px;color:#222">Copyright © 2022 <b>rotavia-demo.se</b>. All Rights Reserved.</p>

</body>
</html>
```